Letterhead for sustainable Last Mile Logistics needed

Dear all,

we are looking for a powerful design for our letterhead. We are a Berlin-based (Germany) logistics company which delivers parcel on the last mile in a sustainable way. Design should communicate: sustainability, integrity, one family, performance-focused, passionate for excellence and customer experience. Please find company logo attached.

Looking forward for

```html
<!DOCTYPE html>
<html lang="en">
<head>
<meta charset="utf-8">
<title>Canopy Freight – Letterhead</title>
<link rel="stylesheet" href="https://fonts.googleapis.com/css2?family=Open+Sans:wght@400;700&display=swap">
<style>
  :root {
    --backdrop: #c4c4c4;
    --paper: #ffffff;
    --brand-green: #1c9e4a;
    --brand-lime: #9ccd3a;
    --ink: #1f1f1f;
  }
  * { margin: 0; padding: 0; box-sizing: border-box; }
  html, body {
    width: 1200px;
    height: 686px;
    overflow: hidden;
    background: var(--backdrop);
  }
  body {
    display: flex;
    align-items: center;
    justify-content: center;
    font-family: "Open Sans", Arial, sans-serif;
  }
  .letterhead {
    position: relative;
    width: 440px;
    height: 622px;
    background: var(--paper);
    box-shadow: 0 6px 24px rgba(0,0,0,0.18);
    overflow: hidden;
  }
  .brand {
    position: absolute;
    top: 38px;
    left: 36px;
    display: flex;
    align-items: center;
    gap: 10px;
  }
  .brand-dot {
    width: 22px;
    height: 22px;
    border-radius: 50%;
    background: var(--brand-green);
  }
  .brand-name {
    font-weight: 700;
    font-size: 21px;
    letter-spacing: 0.5px;
    text-transform: uppercase;
    color: var(--brand-green);
  }
  .contact {
    position: absolute;
    right: 30px;
    top: 272px;
    list-style: none;
    text-align: right;
    color: var(--ink);
    font-size: 11px;
    line-height: 1.45;
  }
  .contact li {
    display: flex;
    justify-content: flex-end;
    align-items: flex-start;
    gap: 7px;
  }
  .contact li + li.group { margin-top: 6px; }
  .contact .icon {
    width: 11px;
    height: 11px;
    flex: none;
    margin-top: 2px;
    fill: var(--brand-green);
  }
  .footer-wave {
    position: absolute;
    left: 0;
    bottom: 0;
    width: 440px;
    height: 240px;
  }
</style>
</head>
<body>
  <main class="letterhead">
    <header class="brand">
      <span class="brand-dot"></span>
      <span class="brand-name">Canopy Freight</span>
    </header>

    <ul class="contact">
      <li>
        <span>27 Linden Row<br>Ashford, Kent, TN9 4QA</span>
        <svg class="icon" viewBox="0 0 12 12" aria-hidden="true"><path d="M6 0a4 4 0 0 0-4 4c0 3 4 8 4 8s4-5 4-8a4 4 0 0 0-4-4zm0 5.6A1.6 1.6 0 1 1 6 2.4a1.6 1.6 0 0 1 0 3.2z"/></svg>
      </li>
      <li class="group">
        <span>(555) 014-3382</span>
        <svg class="icon" viewBox="0 0 12 12" aria-hidden="true"><path d="M2.4 0.6l2 2-1 1.4a7 7 0 0 0 4.6 4.6l1.4-1 2 2-1.4 1.8C5 11 1 7 0.6 2z"/></svg>
      </li>
      <li>
        <span>www.canopyfreight.example</span>
        <svg class="icon" viewBox="0 0 12 12" aria-hidden="true"><circle cx="6" cy="6" r="5.5"/><path d="M0.5 6h11M6 0.5c-2.4 2.6-2.4 8.4 0 11M6 0.5c2.4 2.6 2.4 8.4 0 11" stroke="#fff" stroke-width="0.8" fill="none"/></svg>
      </li>
      <li>
        <span>hello@canopyfreight.example</span>
        <svg class="icon" viewBox="0 0 12 12" aria-hidden="true"><rect x="0" y="2" width="12" height="8.5" rx="1"/><path d="M0.6 2.6L6 7l5.4-4.4" stroke="#fff" stroke-width="0.9" fill="none"/></svg>
      </li>
    </ul>

    <svg class="footer-wave" viewBox="0 0 440 240" aria-hidden="true">
      <path class="wave-accent" d="M0 224 C120 212 205 168 262 112 C318 58 372 26 440 18"
            fill="none" stroke="var(--brand-lime)" stroke-width="5"/>
      <path class="wave-band" d="M0 240 L0 232 C125 224 210 184 268 128 C324 74 378 40 440 32 L440 240 Z"
            fill="var(--brand-green)"/>
    </svg>
  </main>
</body>
</html>
```